The Kestrel Personal Training Studio Information Card

The front and back of card to give people that walk in to our gym. There are a few things to say on the card. But it also needs to be designed in an attractive way. You can make some of the information bullett points or with icons or graphics. Please look at our website at https://thekestrelfitness-example.com/ . The card will be 4" x 9"

Target Market(s)

High End Clientele who want to train in a private gym

Industry/Entity Type

Fitness

Font styles to use
Serif
Sans Serif
Other font styles liked:
• the same font Vorlex uses on the zuntab

Colors
F0912C
F2A743
F7CA91
FBE8D2
FDF5EE

Requirements
Must have
• A cool look

```html
<!DOCTYPE html>
<html lang="en">
<head>
<meta charset="utf-8">
<title>The Kestrel Personal Training Studio – Information Card</title>
<link rel="stylesheet" href="https://fonts.googleapis.com/css2?family=Fredoka:wght@400;500;600&family=Montserrat:wght@400;500;600&display=swap">
<style>
  :root {
    --bg: #ececec;
    --red: #e3202a;
    --red-deep: #cf1219;
    --ink: #4a4a4c;
    --charcoal: #3a3a3c;
    --graphite: #555557;
    --white: #ffffff;
    --paper: #f6f6f6;
  }
  * { box-sizing: border-box; margin: 0; padding: 0; }
  html, body { width: 1200px; height: 1062px; overflow: hidden; background: var(--bg); }
  body { position: relative; font-family: "Montserrat", sans-serif; }

  .card { position: absolute; width: 378px; height: 828px; overflow: hidden; }
  .card--front { left: 98px; top: 106px; background: var(--white); }
  .card--back { left: 575px; top: 100px; background: var(--charcoal); }

  .layer { position: absolute; inset: 0; }
  .card-shapes { position: absolute; inset: 0; width: 100%; height: 100%; }

  /* Front */
  .brand { position: absolute; left: 46px; top: 34px; color: var(--ink); font-family: "Fredoka", sans-serif; font-weight: 600; line-height: 1; }
  .brand__the { font-size: 20px; letter-spacing: 1px; }
  .brand__name { font-size: 52px; letter-spacing: 1px; margin-top: 2px; }
  .tagline { position: absolute; left: 49px; top: 112px; font-family: "Montserrat", sans-serif; font-weight: 600; font-size: 13px; letter-spacing: 5.1px; color: var(--ink); }

  .photo { position: absolute; inset: 0; }
  .photo--front {
    background: linear-gradient(100deg, #e9d2c3 0%, #d9a98e 30%, #c9c4c2 55%, #8d8d90 80%, #d8d8da 100%);
    clip-path: polygon(0 185px, 378px 126px, 378px 417px, 0 358px);
  }
  .photo--back {
    background: radial-gradient(ellipse at 55% 45%, #8a8178 0%, #3d3d40 45%, #1e1f22 100%);
    clip-path: polygon(0 229px, 378px 170px, 378px 490px, 0 431px);
  }

  .headline { position: absolute; left: 40px; top: 410px; border-left: 2px solid var(--white); padding-left: 14px; color: var(--white); font-family: "Fredoka", sans-serif; font-weight: 500; line-height: 1; height: 116px; }
  .headline span { display: block; }
  .headline__small { font-size: 23px; margin-top: 6px; }
  .headline__big { font-size: 33px; font-weight: 600; margin-top: 4px; }
  .headline__mid { font-size: 23px; padding-left: 41px; margin-top: 2px; }
  .headline__big em { font-style: normal; font-size: 22px; font-weight: 500; }

  .body-copy { position: absolute; left: 40px; top: 588px; width: 305px; font-size: 9.6px; line-height: 13px; color: #2d2d2f; }
  .body-copy p + p { margin-top: 6px; }
  .body-copy strong { color: var(--red); font-weight: 600; }

  .phone-pill { position: absolute; display: flex; align-items: center; height: 35px; border-radius: 18px; font-family: "Fredoka", sans-serif; font-weight: 600; font-size: 29px; letter-spacing: .3px; }
  .phone-pill__icon { width: 37px; height: 37px; border-radius: 50%; display: flex; align-items: center; justify-content: center; flex: none; margin-left: -2px; margin-right: 10px; }
  .phone-pill--front { left: 56px; top: 727px; width: 269px; background: var(--red); color: var(--white); }
  .phone-pill--front .phone-pill__icon { background: var(--charcoal); border: 2px solid var(--white); }
  .phone-pill--back { left: 54px; top: 726px; width: 269px; background: var(--white); color: var(--red); }
  .phone-pill--back .phone-pill__icon { background: var(--red); border: 2px solid var(--white); }

  .website { position: absolute; left: 0; width: 100%; text-align: center; color: var(--white); font-family: "Montserrat", sans-serif; font-size: 15.5px; }
  .website strong { font-weight: 600; }
  .card--front .website { top: 773px; }
  .card--back .website { top: 770px; }

  /* Back */
  .callout { position: absolute; left: 38px; top: 43px; width: 300px; height: 31px; border: 1.5px solid var(--white); color: var(--white); font-family: "Fredoka", sans-serif; font-weight: 500; font-size: 20px; text-align: center; line-height: 28px; }
  .callout__tail { position: absolute; right: 24px; bottom: -13px; width: 14px; height: 13px; }
  .intro { position: absolute; left: 40px; top: 95px; width: 298px; text-align: center; color: var(--white); font-size: 9.6px; line-height: 13px; }

  .rates-tab { position: absolute; left: 103px; top: 490px; width: 170px; height: 30px; }
  .rates-tab__label { position: absolute; inset: 0; text-align: center; color: var(--white); font-family: "Fredoka", sans-serif; font-weight: 500; font-size: 21px; line-height: 30px; }
  .rates-note { position: absolute; left: 0; width: 100%; top: 527px; text-align: center; color: var(--white); font-family: "Fredoka", sans-serif; font-weight: 500; font-size: 17px; }

  .rate-list { position: absolute; left: 40px; top: 557px; width: 296px; list-style: none; }
  .rate { display: flex; height: 26px; border: 1.5px solid var(--white); border-radius: 13px; overflow: hidden; margin-bottom: 11.5px; font-family: "Fredoka", sans-serif; font-weight: 600; font-size: 14.5px; line-height: 23px; }
  .rate__freq { width: 154px; background: var(--white); color: var(--red); padding-left: 14px; border-radius: 0 12px 12px 0; position: relative; z-index: 1; }
  .rate__price { flex: 1; background: var(--red); color: var(--white); padding-left: 12px; margin-left: -10px; padding-left: 22px; }

  .partner { position: absolute; left: 0; width: 100%; top: 669px; text-align: center; color: var(--white); font-family: "Fredoka", sans-serif; font-size: 15px; }
  .partner strong { font-weight: 600; }
  .partner-example { position: absolute; left: 50px; width: 278px; top: 701px; text-align: center; color: var(--white); font-size: 6.8px; line-height: 9.5px; }
</style>
</head>
<body>

<!-- Front of card -->
<section class="card card--front">
  <svg class="card-shapes" viewBox="0 0 378 828" aria-hidden="true">
    <polygon points="0,358 378,417 378,514 0,574" fill="var(--red)"/>
    <polygon points="0,769 378,707 378,828 0,828" fill="var(--graphite)"/>
  </svg>

  <div class="brand">
    <div class="brand__the">THE</div>
    <div class="brand__name">KESTREL</div>
  </div>
  <div class="tagline">PRIVATE TRAINING STUDIO</div>

  <div class="photo photo--front" role="img" aria-label="Photo of a muscular male athlete in front of a rack of weight plates in a bright gym"></div>

  <h1 class="headline">
    <span class="headline__small">a Safe and</span>
    <span class="headline__big">Individualized</span>
    <span class="headline__mid">approach to</span>
    <span class="headline__big">Strength <em>training</em></span>
  </h1>

  <div class="body-copy">
    <p><strong>Our clients have different goals:</strong> Build strength, Increase Flexibility, Improve functional and daily movements, Train for an event, or Weight Loss. We will tailor your training program to the specific results you are looking for.</p>
    <p>Some ways of training increase the chance of injury, we do not practice those types of training at The Kestrel. Many of our clients have current or past injuries that can cause problems. We work with them to not aggravate those injuries or allow them to become an obstacle to their workouts.</p>
  </div>

  <div class="phone-pill phone-pill--front">
    <span class="phone-pill__icon">
      <svg width="18" height="18" viewBox="0 0 24 24" aria-hidden="true"><path fill="#fff" d="M6.6 10.8a15.1 15.1 0 0 0 6.6 6.6l2.2-2.2c.3-.3.7-.4 1-.2 1.1.4 2.3.6 3.6.6.6 0 1 .4 1 1V20c0 .6-.4 1-1 1A17 17 0 0 1 3 4c0-.6.4-1 1-1h3.5c.6 0 1 .4 1 1 0 1.3.2 2.5.6 3.6.1.3 0 .7-.2 1z"/></svg>
    </span>
    555.014.2297
  </div>
  <div class="website">www.<strong>TheKestrelFitness-example</strong>.com</div>
</section>

<!-- Back of card -->
<section class="card card--back">
  <svg class="card-shapes" viewBox="0 0 378 828" aria-hidden="true">
    <defs>
      <linearGradient id="back-red" x1="0" y1="0" x2="1" y2="1">
        <stop offset="0" stop-color="#e8262f"/>
        <stop offset="1" stop-color="var(--red-deep)"/>
      </linearGradient>
      <linearGradient id="back-dark" x1="0" y1="0" x2="1" y2="0">
        <stop offset="0" stop-color="#333335"/>
        <stop offset="1" stop-color="#5a5a5c"/>
      </linearGradient>
    </defs>
    <rect x="0" y="0" width="378" height="828" fill="url(#back-dark)"/>
    <polygon points="0,0 378,0 378,170 0,229" fill="url(#back-red)"/>
    <polygon points="0,769 378,708 378,828 0,828" fill="url(#back-red)"/>
  </svg>

  <div class="callout">
    How do you get Started?
    <svg class="callout__tail" viewBox="0 0 14 13" aria-hidden="true"><polygon points="0,0 14,0 2,13" fill="var(--red)"/><polyline points="0,1 2,13 14,1" fill="none" stroke="#fff" stroke-width="1.5"/></svg>
  </div>
  <p class="intro">We schedule prospective clients for a no cost or obligation consultation. At that consultation we will do a movement screen with you. This will allow the trainer to see what level of flexibility and strength you are currently at. You will be able to discuss your goals and other issues (injuries, etc) at that time.</p>

  <div class="photo photo--back" role="img" aria-label="Photo of a woman seated on a bench holding dumbbells in a dark gym"></div>

  <div class="rates-tab">
    <svg width="170" height="30" viewBox="0 0 170 30" aria-hidden="true"><polygon points="0,0 156,0 170,30 14,30" fill="var(--red)"/></svg>
    <h2 class="rates-tab__label">Our Rates:</h2>
  </div>
  <p class="rates-note">All Sessions are 60 minutes</p>

  <ul class="rate-list">
    <li class="rate"><span class="rate__freq">1 time per week:</span><span class="rate__price">$110 per session</span></li>
    <li class="rate"><span class="rate__freq">2 times per week:</span><span class="rate__price">$85 per session</span></li>
    <li class="rate"><span class="rate__freq">3 times per week:</span><span class="rate__price">$80 per session</span></li>
  </ul>

  <p class="partner"><strong>Add $40</strong> for a Partnered Session</p>
  <p class="partner-example">Example: A Partnered Session (2 people training together) coming twice a week is $125 per session</p>

  <div class="phone-pill phone-pill--back">
    <span class="phone-pill__icon">
      <svg width="18" height="18" viewBox="0 0 24 24" aria-hidden="true"><path fill="#fff" d="M6.6 10.8a15.1 15.1 0 0 0 6.6 6.6l2.2-2.2c.3-.3.7-.4 1-.2 1.1.4 2.3.6 3.6.6.6 0 1 .4 1 1V20c0 .6-.4 1-1 1A17 17 0 0 1 3 4c0-.6.4-1 1-1h3.5c.6 0 1 .4 1 1 0 1.3.2 2.5.6 3.6.1.3 0 .7-.2 1z"/></svg>
    </span>
    555.014.2297
  </div>
  <div class="website">www.<strong>TheKestrelFitness-example</strong>.com</div>
</section>

</body>
</html>
```